Online-Marketing Material für einen Online Kurs
Zielgruppe
Online Kurs SerienTitel 'Vom Nebel ins Licht' Untertitel: 'Mach aus Deinem schwersten Tag einen Anfang voller Mut!' Zielgruppe: Menschen mit chronischen Rückenschmerzen
Titel: Chronische Rückenschmerzen
Aufgabenstellung
1. Kleine Änderung des Logos: Bright HoRizons raus und Dr. Lukas Brennwald in leuchtendem grün rein
Es gibt zwei Titel: Serientitel und den Kurstitel
2. Logo und Bild für Online Kurs für kursio und andere Nutzungen, Akzentfarbe soll grün sein. Das Vitalorb Logo kann klein sein, der Titel ist am wichtigsten.
3. Ein Bild sollte für kursio quadratisch sein.
4. Vielleicht eine Foto Collage von Mensch mit Schmerzen und Mensch mit Power

```html
<!DOCTYPE html>
<html lang="de">
<head>
<meta charset="utf-8">
<title>Vom Nebel ins Licht – Chronische Rückenschmerzen</title>
<link href="https://fonts.googleapis.com/css2?family=Roboto:wght@400;500;900&family=Kaushan+Script&display=swap" rel="stylesheet">
<style>
  :root {
    --green: #2aa800;
    --green-bright: #33b810;
    --white: #ffffff;
    --grey-text: #5a5a5a;
    --dark-top: #5c5a5b;
    --dark-bottom: #3d3b3c;
    --photo-warm: #d9d3cb;
    --photo-cool: #c9cfd2;
  }
  html, body {
    margin: 0;
    padding: 0;
    overflow: hidden;
  }
  body {
    width: 1200px;
    height: 1200px;
    font-family: "Roboto", Arial, sans-serif;
  }
  .canvas {
    position: relative;
    width: 1200px;
    height: 1200px;
    overflow: hidden;
    background: var(--white);
  }
  .footer-band {
    position: absolute;
    left: 0; top: 760px;
    width: 1200px; height: 440px;
    background: linear-gradient(180deg, var(--dark-top), var(--dark-bottom));
  }
  .photo {
    position: absolute;
  }
  .photo--desk {
    left: 470px; top: 0;
    width: 730px; height: 452px;
    background: linear-gradient(135deg, #f3f1ee 0%, #e6e2dc 45%, #a9c6c6 80%, #c79a6a 100%);
  }
  .photo--sofa {
    left: 703px; top: 465px;
    width: 497px; height: 453px;
    border-bottom-right-radius: 90px;
    background: linear-gradient(160deg, #eceae7 0%, #d8d3cc 45%, #c9b8a2 75%, #6f7f95 100%);
  }
  .brand {
    position: absolute;
    left: 74px; top: 86px;
    width: 362px;
  }
  .brand__name {
    font-weight: 500;
    font-size: 54px;
    line-height: 1;
    letter-spacing: 1px;
    color: var(--grey-text);
  }
  .brand__person {
    margin-top: 10px;
    text-align: right;
    font-weight: 500;
    font-size: 28px;
    color: var(--green-bright);
  }
  .panel {
    position: absolute;
    left: 0; top: 213px;
    width: 703px; height: 705px;
    background: var(--green);
    border-top-right-radius: 100px;
    border-bottom-left-radius: 100px;
    box-sizing: border-box;
    padding: 70px 0 0 70px;
    color: var(--white);
  }
  .panel__title {
    margin: 0;
    font-weight: 900;
    font-size: 108px;
    line-height: 113px;
    letter-spacing: -1px;
    text-transform: uppercase;
  }
  .panel__subtitle {
    margin: 28px 0 0;
    font-weight: 400;
    font-size: 45px;
    line-height: 72px;
    width: 610px;
  }
  .course-pill {
    position: absolute;
    left: 78px; top: 918px;
    width: 1040px; height: 130px;
    box-sizing: border-box;
    border: 10px solid var(--white);
    border-radius: 65px;
    background: var(--green);
    box-shadow: 0 10px 18px rgba(0,0,0,0.35);
    display: flex;
    align-items: center;
    justify-content: center;
  }
  .course-pill__title {
    margin: 0;
    font-family: "Kaushan Script", cursive;
    font-weight: 400;
    font-size: 66px;
    color: var(--white);
  }
  .web {
    position: absolute;
    left: 0; top: 1086px;
    width: 1200px;
    display: flex;
    justify-content: center;
    align-items: center;
    gap: 16px;
    color: var(--white);
    font-weight: 500;
    font-size: 37px;
    letter-spacing: 6px;
  }
  .web__icon { width: 32px; height: 32px; }
</style>
</head>
<body>
  <div class="canvas">
    <div class="footer-band"></div>

    <div class="photo photo--desk" role="img" aria-label="Foto: Frau am Schreibtisch mit Laptop hält sich den schmerzenden unteren Rücken"></div>
    <div class="photo photo--sofa" role="img" aria-label="Foto: älterer Mann mit Brille auf dem Sofa hält sich die schmerzende Schulter"></div>

    <div class="brand">
      <div class="brand__name">VITALORB</div>
      <div class="brand__person">Dr. Lukas Brennwald</div>
    </div>

    <section class="panel">
      <h1 class="panel__title">Vom<br>Nebel<br>ins Licht</h1>
      <p class="panel__subtitle">Mach aus Deinem schwersten Tag einen Anfang voller Mut!</p>
    </section>

    <div class="course-pill">
      <h2 class="course-pill__title">Chronische Rückenschmerzen</h2>
    </div>

    <div class="web">
      <svg class="web__icon" viewBox="0 0 32 32" aria-hidden="true">
        <g fill="none" stroke="#2aa800" stroke-width="2.4">
          <circle cx="16" cy="16" r="13"/>
          <ellipse cx="16" cy="16" rx="6" ry="13"/>
          <line x1="3" y1="16" x2="29" y2="16"/>
          <line x1="5" y1="9" x2="27" y2="9"/>
          <line x1="5" y1="23" x2="27" y2="23"/>
        </g>
      </svg>
      <span class="web__url">www.vitalorb.de</span>
    </div>
  </div>
</body>
</html>
```